quiet meadow therapy (QMT)

I need to build a website for my therapy business.
There are two parts to the website
on the landing page; they choose whether they are therapists making a referral or patients needing more information.
After that, they are taken to their respective pages.
There is the textual information and a referral form on the therapist page, and on the patient page, the text is a bit different, and there will be a booking page on the patient page.
Visually minimal, it's a therapeutic website. I want it clean, clinical, and modern
colors: greenish blue or maybe orangish
PHP/html code
Updates

Hi everyone
I'm very sorry for the lack of responses to your designs. I am trying to work it out, but this platform has been a challenge for me.
I appreciate everyone's efforts, and I am unsure how to rate designs and move forward with the ones I like. There is a 5-star rating, but I don't understand how I'm supposed to politely say that it is not it without feeling like I'm going to affect someone's future rating negatively.
Please understand me. Thank you

Designs look the same

Target Market(s)

therapy and stress management

Industry/Entity Type

stress management therapy

Coding

Coded - Design and coding required

Number of Pages Required

5+ page

Font styles to use
Serif

Colors
0094D4
00A9DD
6FCCEA
C7EBF8
E9F6FB
00AB8E
00BBA5
67D7C9
C6EFE9
E9F9F6

Requirements
Must have
• landing page that that have 2 options. one for therapist another for patient

```html
<!DOCTYPE html>
<html lang="en">
<head>
<meta charset="utf-8">
<title>Quiet Meadow Therapy</title>
<link href="https://fonts.googleapis.com/css2?family=Poppins:wght@300;400;500;600;700&display=swap" rel="stylesheet">
<style>
:root{
  --blue:#0094D4;
  --blue-2:#00A9DD;
  --teal:#00AB8E;
  --teal-2:#1DB8A0;
  --teal-soft:#67D7C9;
  --mint:#EAF8F6;
  --mint-2:#C6EFE9;
  --orange:#F7941D;
  --ink:#1F2A2E;
  --ink-soft:#4A5558;
  --white:#FFFFFF;
  --line:#D4E3E0;
}
*{box-sizing:border-box;margin:0;padding:0}
html,body{width:1200px;height:4847px;overflow:hidden;background:var(--mint)}
body{font-family:'Poppins',sans-serif;color:var(--ink)}
.canvas{position:relative;width:1200px;height:4847px;overflow:hidden;background:var(--mint)}
.abs{position:absolute}
.btn{position:absolute;display:flex;align-items:center;justify-content:center;border-radius:20px;color:var(--white);font-size:13px;font-weight:500;white-space:nowrap}
.btn-teal{background:var(--teal-2)}
.btn-blue{background:var(--blue)}
.center-x{left:0;width:1200px;text-align:center}

/* header */
.site-header{position:absolute;left:0;top:0;width:1200px;height:135px;background:var(--mint)}
.brand{position:absolute;left:75px;top:26px;display:flex;align-items:center;gap:12px}
.brand-dot{width:44px;height:44px;border-radius:50%;background:var(--teal-2)}
.brand-name{font-size:50px;font-weight:500;letter-spacing:10px;line-height:1;color:var(--ink)}
.brand-tag{position:absolute;left:80px;top:91px;font-size:10px;font-weight:500;letter-spacing:1.5px;color:var(--ink)}
.contact-chip{position:absolute;top:36px;display:flex;align-items:center;gap:10px}
.chip-icon{width:26px;height:26px;border-radius:50%;background:var(--teal-2);display:flex;align-items:center;justify-content:center}
.chip-label{font-size:11px;color:var(--teal);line-height:1.1}
.chip-value{font-size:12px;color:var(--ink);line-height:1.2}
.main-nav{position:absolute;top:86px;left:0;width:1200px;height:24px;font-size:13px;color:var(--ink)}
.main-nav span{position:absolute;top:0}
.main-nav .active{color:var(--teal)}
.nav-mark{position:absolute;left:522px;top:131px;width:38px;height:4px;background:var(--teal-2);border-radius:2px}

/* hero */
.hero{position:absolute;left:0;top:135px;width:1200px;height:636px;background:linear-gradient(100deg,#BFCBCD 0%,#DADFDD 30%,#CDBBAA 60%,#E2E4E0 100%)}
.hero-title-top{position:absolute;top:382px;font-size:32px;font-weight:600;letter-spacing:4px;color:var(--white)}
.hero-title{position:absolute;top:422px;font-size:35px;letter-spacing:3px;font-weight:300;color:var(--white)}
.hero-title b{font-weight:700}
.hero-sub{position:absolute;top:472px;left:400px;width:420px;text-align:center;font-size:15px;line-height:19px;color:var(--white)}
.slide-num{position:absolute;left:40px;width:20px;text-align:center;font-size:10px;color:var(--white)}
.slide-num.on{left:30px;width:38px;height:38px;border-radius:50%;background:#D99A52;line-height:38px}

/* welcome */
.section-line{position:absolute;height:3px;background:var(--teal-2)}
.h2{position:absolute;font-size:28px;font-weight:400;letter-spacing:2px;color:var(--ink)}
.h2 b{font-weight:600}
.body-text{font-size:13.5px;line-height:21.5px;color:var(--ink-soft)}
.stat{position:absolute;top:1213px;display:flex;gap:14px}
.stat-icon{width:44px;height:44px;border-radius:50%;background:var(--teal-2);display:flex;align-items:center;justify-content:center;flex:none}
.stat-num{font-size:17px;font-weight:600;color:var(--ink);line-height:22px}
.stat-text{font-size:13px;line-height:22px;color:var(--ink-soft)}

/* services */
.services{position:absolute;left:0;top:1529px;width:1200px;height:728px;background:var(--blue)}
.card{position:absolute;background:var(--white);border-radius:8px;overflow:hidden}
.card-img{width:100%}
.card-title{position:absolute;left:0;width:100%;text-align:center;font-size:17px;font-weight:500;line-height:23px;color:var(--ink)}
.card-text{position:absolute;left:0;width:100%;text-align:center;font-size:12.5px;line-height:15px;color:var(--ink-soft)}
.chev{position:absolute}

/* how it works */
.step-ring{position:absolute;width:170px;height:170px;border-radius:50%;background:var(--white);box-shadow:6px 8px 14px rgba(0,0,0,.08)}
.step-core{position:absolute;width:106px;height:106px;border-radius:50%;display:flex;align-items:center;justify-content:center}
.step-num{position:absolute;font-size:150px;font-weight:700;line-height:1;color:transparent;-webkit-text-stroke:2px #C3CCCC}
.step-title{position:absolute;width:330px;text-align:center;font-size:18px;font-weight:500;color:var(--ink)}
.step-text{position:absolute;width:330px;text-align:center;font-size:12.5px;line-height:15px;color:var(--ink-soft)}

/* testimonials */
.testimonial{position:absolute;left:115px;top:2866px;width:972px;height:345px;border-radius:12px;background:linear-gradient(90deg,#2CA690 0%,#30B8A3 45%,#2FB7A2 65%,#33A892 100%);overflow:hidden}
.t-arrow{position:absolute;width:48px;height:48px;border-radius:50%;background:rgba(255,255,255,.25);display:flex;align-items:center;justify-content:center}

/* blog */
.blog-card{position:absolute;background:var(--white);border:2px solid #D9E6E3;border-radius:8px;overflow:hidden}
.date-badge{position:absolute;width:56px;height:56px;border-radius:50%;background:var(--teal-2);color:var(--white);font-size:12px;line-height:15px;text-align:center;padding-top:12px}
.blog-title{position:absolute;left:30px;width:250px;font-size:13px;font-weight:600;line-height:18px;color:var(--ink)}
.blog-rule{position:absolute;left:30px;width:44px;height:2px;background:var(--teal-2)}
.blog-text{position:absolute;left:30px;width:250px;font-size:12.5px;line-height:15px;color:var(--ink-soft)}

/* form */
.field{position:absolute;height:33px;background:var(--white);border:1px solid #D3DEDC;border-radius:3px;font-size:11px;color:var(--ink-soft);padding:9px 12px}
.field .caret{position:absolute;right:12px;top:9px;font-size:10px}

/* footer */
.site-footer{position:absolute;left:0;top:4413px;width:1200px;height:367px;background:var(--blue);color:var(--white)}
.f-head{position:absolute;font-size:16px;font-weight:600}
.f-rule{position:absolute;width:58px;height:2px;background:var(--white)}
.f-item{position:absolute;font-size:13px;line-height:18px}
.bottom-bar{position:absolute;left:0;top:4780px;width:1200px;height:67px;background:var(--mint)}
.social{position:absolute;top:17px;width:36px;height:36px;border-radius:50%;background:var(--ink)}
</style>
</head>
<body>
<div class="canvas">

  <header class="site-header">
    <div class="brand">
      <div class="brand-dot"></div>
      <div class="brand-name">QMT</div>
    </div>
    <div class="brand-tag">QUIET MEADOW THERAPY</div>

    <div class="contact-chip" style="left:602px">
      <div class="chip-icon">
        <svg width="14" height="14" viewBox="0 0 24 24"><path d="M6.6 10.8a15 15 0 0 0 6.6 6.6l2.2-2.2a1 1 0 0 1 1-.25 11.4 11.4 0 0 0 3.6.57 1 1 0 0 1 1 1V20a1 1 0 0 1-1 1A17 17 0 0 1 3 4a1 1 0 0 1 1-1h3.5a1 1 0 0 1 1 1c0 1.25.2 2.45.57 3.57a1 1 0 0 1-.25 1z" fill="#fff"/></svg>
      </div>
      <div><div class="chip-label">Call Us</div><div class="chip-value">555 010 2468</div></div>
    </div>
    <div class="contact-chip" style="left:760px">
      <div class="chip-icon">
        <svg width="14" height="14" viewBox="0 0 24 24"><rect x="3" y="5" width="18" height="14" rx="2" fill="#fff"/><path d="M3 6l9 7 9-7" stroke="#1DB8A0" stroke-width="2" fill="none"/></svg>
      </div>
      <div><div class="chip-label">Email us</div><div class="chip-value">hello@qmt.example</div></div>
    </div>
    <div class="btn btn-blue" style="left:950px;top:32px;width:175px;height:34px">Fix An Appointment</div>

    <nav class="main-nav">
      <span class="active" style="left:522px">Home</span>
      <span style="left:610px">About us</span>
      <span style="left:720px">Our Services ⌄</span>
      <span style="left:855px">Blog</span>
      <span style="left:935px">Therapist</span>
      <span style="left:1048px">Contact us</span>
    </nav>
    <div class="nav-mark"></div>
  </header>

  <section class="hero" role="img" aria-label="Photo of a therapist in conversation with a smiling client on a sofa in a bright room"></section>
  <div class="hero-title-top center-x">QUIET</div>
  <div class="hero-title center-x">MEADOW <b>THERAPY</b></div>
  <div class="hero-sub">Lorem Ipsum is simply dummy text industrya print typesetting industry</div>
  <div class="btn btn-blue" style="left:500px;top:534px;width:192px;height:38px">Fix An Appointment</div>

  <div class="slide-num" style="top:372px">01</div>
  <div class="slide-num on" style="top:399px">02</div>
  <div class="slide-num" style="top:458px">03</div>
  <div class="slide-num" style="top:495px">04</div>

  <svg class="abs" style="left:0;top:700px" width="1200" height="120" viewBox="0 0 1200 120">
    <path d="M0 60 C150 80 300 90 450 55 C600 20 700 10 850 30 C1000 50 1100 50 1200 40 L1200 120 L0 120 Z" fill="#EAF8F6"/>
  </svg>
  <div class="abs" style="left:576px;top:743px;width:56px;height:56px;border-radius:50%;background:var(--white);box-shadow:0 4px 10px rgba(0,0,0,.12);display:flex;align-items:center;justify-content:center">
    <svg width="18" height="28" viewBox="0 0 18 28"><path d="M9 2v22M2 17l7 8 7-8" stroke="#1F2A2E" stroke-width="2" fill="none"/></svg>
  </div>

  <!-- welcome: entry choice between therapist referral and patient information -->
  <svg class="abs" style="left:170px;top:895px" width="360" height="505" viewBox="0 0 360 505" role="img" aria-label="Photo of a therapist talking with a seated young man">
    <defs>
      <linearGradient id="welcomeFill" x1="0" y1="0" x2="0" y2="1">
        <stop offset="0" stop-color="#A9D9D3"/>
        <stop offset="0.55" stop-color="#6FB3B4"/>
        <stop offset="1" stop-color="#3E7F9A"/>
      </linearGradient>
    </defs>
    <circle cx="178" cy="167" r="163" fill="url(#welcomeFill)"/>
    <circle cx="178" cy="346" r="150" fill="url(#welcomeFill)"/>
    <path d="M330 400 a30 30 0 0 1 -20 42" stroke="#1F2A2E" stroke-width="1.5" fill="none"/>
  </svg>

  <div class="section-line" style="left:590px;top:992px;width:66px"></div>
  <div class="h2" style="left:628px;top:940px">WELCOME <b>TO QMT</b></div>
  <p class="body-text abs" style="left:628px;top:1015px;width:465px">Lorem Ipsum is simply dummy text of the printing and typesetting industry has been the industry's standard dummy text ever since the 1500s,</p>
  <p class="body-text abs" style="left:628px;top:1101px;width:465px">when an unknown printer took a galley of type and scrambled it to make a type specimen book. It has survived not only five centuries, but also the leap into electronic typesetting, remaining essentially unchanged. It was popularised in the 1960s</p>

  <div class="stat" style="left:623px">
    <div class="stat-icon"><svg width="20" height="20" viewBox="0 0 24 24"><path d="M2 10h4v11H2zM8 21h9a2 2 0 0 0 2-1.5l2-7A2 2 0 0 0 19 10h-5l1-5a2 2 0 0 0-3.5-1.5L8 9z" fill="#fff"/></svg></div>
    <div><div class="stat-num">95%</div><div class="stat-text">Increased Satisfaction<br>With Life</div></div>
  </div>
  <div class="stat" style="left:853px">
    <div class="stat-icon"><svg width="22" height="22" viewBox="0 0 24 24"><circle cx="12" cy="12" r="9" fill="none" stroke="#fff" stroke-width="2"/><path d="M8 14a5 5 0 0 0 8 0" stroke="#fff" stroke-width="2" fill="none"/><circle cx="9" cy="10" r="1.3" fill="#fff"/><circle cx="15" cy="10" r="1.3" fill="#fff"/></svg></div>
    <div><div class="stat-num">75%</div><div class="stat-text">Behavior Recovery after<br>22 Sessions</div></div>
  </div>

  <a class="btn btn-teal path-therapist" style="left:624px;top:1317px;width:155px;height:38px;text-decoration:none">I'm A Therapist</a>
  <a class="btn btn-blue path-patient" style="left:792px;top:1317px;width:199px;height:38px;text-decoration:none">I'm A Patient</a>

  <section class="services">
    <div class="h2 center-x" style="top:68px;color:#fff">OUR <b>SERVICES</b></div>

    <div class="card" style="left:115px;top:147px;width:301px;height:440px">
      <div class="card-img" style="height:244px;background:linear-gradient(120deg,#B7C7D3,#E6E8EA 50%,#C9B9A6)" role="img" aria-label="Photo of a relaxed client talking with a therapist who takes notes"></div>
      <div class="card-title" style="top:284px">Stress Management<br>Therapy</div>
      <div class="card-text" style="top:348px">Lorem Ipsum is simply dummy text<br>industrya print typesetting.</div>
      <svg class="chev" style="left:137px;top:399px" width="28" height="14" viewBox="0 0 28 14"><path d="M2 2l6 5-6 5M11 2l6 5-6 5M20 2l6 5-6 5" stroke="#1DB8A0" stroke-width="2.2" fill="none"/></svg>
    </div>

    <div class="card" style="left:448px;top:147px;width:302px;height:440px">
      <div class="card-img" style="height:244px;background:linear-gradient(120deg,#E9ECEE,#C5CDD6 50%,#3B4A66)" role="img" aria-label="Photo of a woman resting in a large armchair by a window"></div>
      <div class="card-title" style="top:284px">Health Care<br>Therapeutic</div>
      <div class="card-text" style="top:348px">Lorem Ipsum is simply dummy text<br>industrya print typesetting.</div>
      <svg class="chev" style="left:137px;top:399px" width="28" height="14" viewBox="0 0 28 14"><path d="M2 2l6 5-6 5M11 2l6 5-6 5M20 2l6 5-6 5" stroke="#1DB8A0" stroke-width="2.2" fill="none"/></svg>
    </div>

    <div class="card" style="left:786px;top:147px;width:301px;height:440px">
      <div class="card-img" style="height:244px;background:linear-gradient(120deg,#F1F1EE,#D9D6D0 50%,#45506A)" role="img" aria-label="Photo of a tired woman at a desk with a laptop and open book"></div>
      <div class="card-title" style="top:284px">Depression<br>Treatment</div>
      <div class="card-text" style="top:348px">Lorem Ipsum is simply dummy text<br>industrya print typesetting.</div>
      <svg class="chev" style="left:137px;top:399px" width="28" height="14" viewBox="0 0 28 14"><path d="M2 2l6 5-6 5M11 2l6 5-6 5M20 2l6 5-6 5" stroke="#1DB8A0" stroke-width="2.2" fill="none"/></svg>
    </div>

    <div class="btn btn-teal" style="left:528px;top:625px;width:153px;height:37px">View More</div>
  </section>

  <div class="h2 center-x" style="top:2362px">HOW <b>IT WORKS</b></div>

  <div class="step-num" style="left:158px;top:2436px">1</div>
  <div class="step-ring" style="left:180px;top:2436px"></div>
  <div class="step-core" style="left:212px;top:2468px;background:var(--orange)">
    <svg width="40" height="40" viewBox="0 0 24 24"><path d="M13 2L5 13h6l-1 9 8-11h-6z" fill="#fff"/></svg>
  </div>
  <div class="step-title" style="left:93px;top:2640px">1st Phase</div>
  <div class="step-text" style="left:93px;top:2685px">Lorem Ipsum is simply dummy text<br>industrya print typesetting.</div>

  <div class="step-num" style="left:492px;top:2436px">2</div>
  <div class="step-ring" style="left:513px;top:2436px"></div>
  <div class="step-core" style="left:545px;top:2468px;background:var(--blue)">
    <svg width="40" height="40" viewBox="0 0 24 24"><circle cx="12" cy="12" r="9" fill="none" stroke="#fff" stroke-width="2"/><path d="M9.5 9.5a2.5 2.5 0 1 1 3.5 2.3c-.7.3-1 .9-1 1.7" stroke="#fff" stroke-width="2" fill="none"/><circle cx="12" cy="17" r="1.2" fill="#fff"/></svg>
  </div>
  <div class="step-title" style="left:433px;top:2640px">1st Phase</div>
  <div class="step-text" style="left:433px;top:2685px">Lorem Ipsum is simply dummy text<br>industrya print typesetting.</div>

  <div class="step-num" style="left:810px;top:2436px">3</div>
  <div class="step-ring" style="left:831px;top:2436px"></div>
  <div class="step-core" style="left:863px;top:2468px;background:var(--teal-2)">
    <svg width="40" height="40" viewBox="0 0 24 24"><path d="M4 12l5 5L20 6" stroke="#fff" stroke-width="2.5" fill="none"/></svg>
  </div>
  <div class="step-title" style="left:751px;top:2640px">Final Phase</div>
  <div class="step-text" style="left:751px;top:2685px">Lorem Ipsum is simply dummy text<br>industrya print typesetting.</div>

  <div class="btn btn-teal" style="left:528px;top:2759px;width:153px;height:38px">View More</div>

  <section class="testimonial" role="img" aria-label="Soft teal-tinted photo of a therapy session in the background">
    <div class="abs" style="left:0;top:44px;width:972px;text-align:center;font-size:28px;font-weight:600;letter-spacing:2px;color:#fff">TESTIMONIALS</div>
    <div class="abs" style="left:0;top:88px;width:972px;text-align:center;font-size:12.5px;line-height:15px;color:#fff">Professional, licensed, and vetted therapists<br>who you can trust</div>
    <svg class="abs" style="left:471px;top:136px" width="30" height="22" viewBox="0 0 30 22"><path d="M6 0h8l-6 22H0zM20 0h8l-6 22h-8z" fill="#fff"/></svg>
    <div class="abs" style="left:0;top:164px;width:972px;text-align:center;font-size:17px;font-weight:600;color:#fff">Nora Vale</div>
    <div class="abs" style="left:256px;top:194px;width:460px;text-align:center;font-size:13.5px;line-height:22px;color:#fff">Lorem Ipsum is simply dummy text of the printing and typesetting industry has been the industry's standard dummy text ever since the 1500s,</div>
    <div class="abs" style="left:0;top:264px;width:972px;text-align:center;font-size:15px;letter-spacing:4px;color:var(--orange)">★★★★★</div>
    <div class="abs" style="left:441px;top:301px;width:8px;height:8px;border-radius:50%;background:#fff"></div>
    <div class="abs" style="left:460px;top:301px;width:34px;height:8px;border-radius:4px;background:#fff"></div>
    <div class="abs" style="left:506px;top:301px;width:8px;height:8px;border-radius:50%;background:#fff"></div>
    <div class="abs" style="left:525px;top:301px;width:8px;height:8px;border-radius:50%;background:#fff"></div>
    <div class="t-arrow" style="left:188px;top:187px"><svg width="14" height="14" viewBox="0 0 14 14"><path d="M9 2L4 7l5 5" stroke="#fff" stroke-width="2" fill="none"/></svg></div>
    <div class="t-arrow" style="left:764px;top:187px"><svg width="14" height="14" viewBox="0 0 14 14"><path d="M5 2l5 5-5 5" stroke="#fff" stroke-width="2" fill="none"/></svg></div>
  </section>

  <div class="center-x abs" style="top:3294px;font-size:28px;font-weight:600;letter-spacing:2px">BLOG</div>
  <div class="center-x abs" style="top:3336px;font-size:13px;color:var(--ink-soft)">Recent Articles</div>

  <article class="blog-card" style="left:115px;top:3374px;width:301px;height:441px">
    <div style="height:245px;background:linear-gradient(120deg,#B7C7D3,#E6E8EA 50%,#C9B9A6)" role="img" aria-label="Photo of a client talking with a note-taking therapist"></div>
    <div class="date-badge" style="left:19px;top:213px">1st<br>Aug</div>
    <div class="blog-title" style="top:283px">Mental Health/Behavioral Concerns &amp; Symptoms</div>
    <div class="blog-rule" style="top:324px"></div>
    <div class="blog-text" style="top:343px">Lorem Ipsum is simply dummy text industry a print typesetting.</div>
    <svg class="chev" style="left:30px;top:400px" width="22" height="12" viewBox="0 0 22 12"><path d="M2 2l5 4-5 4M9 2l5 4-5 4M16 2l5 4-5 4" stroke="#1DB8A0" stroke-width="2" fill="none"/></svg>
  </article>

  <article class="blog-card" style="left:448px;top:3374px;width:302px;height:441px">
    <div style="height:245px;background:linear-gradient(120deg,#E9ECEE,#C5CDD6 50%,#3B4A66)" role="img" aria-label="Photo of a woman resting in a large armchair"></div>
    <div class="date-badge" style="left:19px;top:213px">1st<br>Aug</div>
    <div class="blog-title" style="top:283px">Let me help you overcome challenges</div>
    <div class="blog-rule" style="top:324px"></div>
    <div class="blog-text" style="top:343px">Lorem Ipsum is simply dummy text industry a print typesetting.</div>
    <svg class="chev" style="left:30px;top:400px" width="22" height="12" viewBox="0 0 22 12"><path d="M2 2l5 4-5 4M9 2l5 4-5 4M16 2l5 4-5 4" stroke="#1DB8A0" stroke-width="2" fill="none"/></svg>
  </article>

  <article class="blog-card" style="left:786px;top:3374px;width:301px;height:441px">
    <div style="height:245px;background:linear-gradient(120deg,#F1F1EE,#D9D6D0 50%,#45506A)" role="img" aria-label="Photo of a tired woman at a desk with a laptop"></div>
    <div class="date-badge" style="left:19px;top:213px">1st<br>Aug</div>
    <div class="blog-title" style="top:283px">Tips for management therapy How to Get Stress Relief</div>
    <div class="blog-rule" style="top:324px"></div>
    <div class="blog-text" style="top:343px">Lorem Ipsum is simply dummy text industry a print typesetting.</div>
    <svg class="chev" style="left:30px;top:400px" width="22" height="12" viewBox="0 0 22 12"><path d="M2 2l5 4-5 4M9 2l5 4-5 4M16 2l5 4-5 4" stroke="#1DB8A0" stroke-width="2" fill="none"/></svg>
  </article>

  <div class="btn btn-teal" style="left:528px;top:3848px;width:153px;height:38px">View More</div>

  <div class="center-x abs" style="top:3962px;font-size:29px;font-weight:600;letter-spacing:2px">REQUEST APPOINTMENT</div>
  <div class="center-x abs" style="top:4006px;font-size:13px;color:var(--ink-soft)">Change your life for better!</div>

  <div class="field" style="left:284px;top:4050px;width:203px">First Name*</div>
  <div class="field" style="left:504px;top:4050px;width:203px">Last Name*</div>
  <div class="field" style="left:724px;top:4050px;width:196px">Email Address*</div>
  <div class="field" style="left:284px;top:4095px;width:203px">Phone*</div>
  <div class="field" style="left:504px;top:4095px;width:203px">Choose Date<span class="caret">⌄</span></div>
  <div class="field" style="left:724px;top:4095px;width:196px">Time<span class="caret">⌄</span></div>
  <div class="field" style="left:284px;top:4140px;width:636px;height:122px">Message</div>

  <div class="btn btn-teal" style="left:528px;top:4287px;width:153px;height:38px">View More</div>

  <footer class="site-footer">
    <div class="abs" style="left:115px;top:128px;display:flex;align-items:center;gap:12px">
      <div style="width:42px;height:42px;border-radius:50%;background:var(--teal-2)"></div>
      <div style="font-size:48px;font-weight:500;letter-spacing:10px;line-height:1;color:#fff">QMT</div>
    </div>
    <div class="abs" style="left:120px;top:190px;font-size:10px;font-weight:500;letter-spacing:1.5px;color:#fff">QUIET MEADOW THERAPY</div>

    <div class="f-head" style="left:389px;top:102px">Quick Links</div>
    <div class="f-rule" style="left:389px;top:138px"></div>
    <div class="f-item" style="left:389px;top:158px">&gt;&nbsp; Home</div>
    <div class="f-item" style="left:389px;top:181px">&gt;&nbsp; About us</div>
    <div class="f-item" style="left:389px;top:203px">&gt;&nbsp; Our Services</div>
    <div class="f-item" style="left:389px;top:226px">&gt;&nbsp; Blog</div>
    <div class="f-item" style="left:389px;top:249px">&gt;&nbsp; Contact us</div>

    <div class="f-head" style="left:566px;top:102px">Contact Detail</div>
    <div class="f-rule" style="left:566px;top:138px"></div>
    <svg class="abs" style="left:566px;top:163px" width="12" height="12" viewBox="0 0 24 24"><path d="M6.6 10.8a15 15 0 0 0 6.6 6.6l2.2-2.2a1 1 0 0 1 1-.25 11.4 11.4 0 0 0 3.6.57 1 1 0 0 1 1 1V20a1 1 0 0 1-1 1A17 17 0 0 1 3 4a1 1 0 0 1 1-1h3.5a1 1 0 0 1 1 1c0 1.25.2 2.45.57 3.57a1 1 0 0 1-.25 1z" fill="#fff"/></svg>
    <div class="f-item" style="left:590px;top:160px">555 010 2468</div>
    <svg class="abs" style="left:566px;top:195px" width="12" height="12" viewBox="0 0 24 24"><rect x="2" y="5" width="20" height="14" rx="2" fill="#fff"/></svg>
    <div class="f-item" style="left:590px;top:192px">care@quietmeadow.example</div>
    <svg class="abs" style="left:566px;top:229px" width="12" height="14" viewBox="0 0 24 28"><path d="M12 0a9 9 0 0 0-9 9c0 7 9 19 9 19s9-12 9-19a9 9 0 0 0-9-9zm0 12a3 3 0 1 1 0-6 3 3 0 0 1 0 6z" fill="#fff"/></svg>
    <div class="f-item" style="left:590px;top:226px">48 Linden Row<br>Suite 210, Fairhaven, GA 30000</div>

    <div class="f-head" style="left:841px;top:102px">Newsletter</div>
    <div class="f-rule" style="left:841px;top:138px"></div>
    <div class="f-item" style="left:841px;top:160px">Lorem Ipsum is simply dummy printing</div>
    <div class="abs" style="left:841px;top:186px;width:246px;height:34px;border-radius:17px;background:#fff;color:var(--ink-soft);font-size:11px;font-style:italic;padding:9px 20px">Email Address</div>
    <div class="abs" style="left:841px;top:227px;width:246px;height:32px;border-radius:16px;background:var(--teal-2);color:#fff;font-size:12px;display:flex;align-items:center;justify-content:center">Subscribe</div>
  </footer>

  <div class="bottom-bar">
    <div class="abs" style="left:115px;top:24px;font-size:12px;color:var(--ink-soft)">Copyright © 2022 <b style="color:var(--ink)">QUIET MEADOW THERAPY</b>. All Rights Reserved.</div>
    <div class="social" style="left:949px;background:var(--teal-2)" role="img" aria-label="Social profile link"></div>
    <div class="social" style="left:996px" role="img" aria-label="Social profile link"></div>
    <div class="social" style="left:1045px" role="img" aria-label="Social profile link"></div>
    <div class="social" style="left:1092px" role="img" aria-label="Social profile link"></div>
  </div>

</div>
</body>
</html>
```